RJK Entertainment

Logo for business card design

Target Market(s)

potential film investors and screenwriters

Industry/Entity Type

Business

Contact Information for Business Card

as shown, website here is a placeholder position

Requirements
Must have
• great visual appeal
Nice to have
• harmony of colors; must evoke spirit of
• U.S.-China cooperation

```html
<!DOCTYPE html>
<html lang="en">
<head>
<meta charset="utf-8">
<title>RJK Entertainment – Business Card</title>
<link rel="stylesheet" href="https://fonts.googleapis.com/css2?family=PT+Sans:wght@400;700&display=swap">
<style>
  :root {
    --backdrop: #939496;
    --card-front: #f6f6f4;
    --card-back-top: #919294;
    --card-back-bottom: #7f8082;
    --brand-red: #cc1f24;
    --brand-yellow: #e3bd12;
    --brand-navy: #1b1f7c;
    --ink: #1d1d1d;
    --rule: #b9b9bb;
    --logo-light: #e6edf2;
  }
  * { box-sizing: border-box; margin: 0; padding: 0; }
  html, body {
    width: 1105px; height: 1200px; overflow: hidden;
    background: var(--backdrop);
    font-family: "PT Sans", sans-serif;
  }
  .canvas { position: relative; width: 1105px; height: 1200px; }
  .card {
    position: absolute; left: 184px; width: 746px; height: 425px;
  }
  .card--front { top: 120px; background: var(--card-front); }
  .card--back {
    top: 637px;
    background: linear-gradient(180deg, var(--card-back-top), var(--card-back-bottom));
  }

  .brand {
    position: absolute; display: flex; align-items: center; gap: 12px;
    font-weight: 700; font-size: 40px; line-height: 1; white-space: nowrap;
  }
  .brand__mark { width: 30px; height: 30px; background: var(--brand-red); flex: none; }
  .card--front .brand { right: 44px; top: 98px; color: var(--brand-navy); }
  .card--back .brand {
    left: 50%; top: 50%; transform: translate(-50%, -50%); color: var(--logo-light);
  }

  .person { position: absolute; left: 43px; top: 214px; }
  .person__name { font-size: 26px; font-weight: 700; color: var(--brand-red); line-height: 1.2; }
  .person__title { font-size: 20px; color: var(--brand-navy); line-height: 1.3; }
  .divider {
    position: absolute; left: 182px; right: 44px; top: 262px;
    height: 1px; background: var(--rule);
  }

  .contact-list { position: absolute; left: 43px; top: 292px; list-style: none; }
  .contact-list li {
    display: flex; align-items: center; gap: 11px;
    font-size: 19px; color: var(--ink); height: 29px;
  }
  .contact-list svg { width: 17px; height: 17px; fill: var(--brand-red); flex: none; }

  .address {
    position: absolute; right: 44px; top: 292px;
    font-style: normal; text-align: right; font-size: 19px; color: var(--ink);
  }
  .address span { display: block; height: 29px; line-height: 29px; }

  .stripes { position: absolute; left: 0; right: 0; top: 394px; height: 4px; display: flex; }
  .stripes i { flex: 1; }
  .stripes .red { background: var(--brand-red); }
  .stripes .yellow { background: var(--brand-yellow); }
  .stripes .navy { background: var(--brand-navy); }
</style>
</head>
<body>
<main class="canvas">
  <section class="card card--front" aria-label="Business card front">
    <div class="brand"><span class="brand__mark"></span>RJK Entertainment</div>

    <div class="person">
      <p class="person__name">Daniel Hart</p>
      <p class="person__title">CEO/Founder</p>
    </div>
    <div class="divider"></div>

    <ul class="contact-list">
      <li>
        <svg viewBox="0 0 24 24" aria-hidden="true"><path d="M6.6 10.8a15.1 15.1 0 0 0 6.6 6.6l2.2-2.2c.3-.3.7-.4 1-.2 1.1.4 2.3.6 3.6.6.6 0 1 .4 1 1V20c0 .6-.4 1-1 1A17 17 0 0 1 3 4c0-.6.4-1 1-1h3.5c.6 0 1 .4 1 1 0 1.3.2 2.5.6 3.6.1.3 0 .7-.2 1z"/></svg>
        555 210 4417
      </li>
      <li>
        <svg viewBox="0 0 24 24" aria-hidden="true"><path d="M7 1h10a2 2 0 0 1 2 2v18a2 2 0 0 1-2 2H7a2 2 0 0 1-2-2V3a2 2 0 0 1 2-2zm0 3v14h10V4zm5 15.5a1.2 1.2 0 1 0 0 2.4 1.2 1.2 0 0 0 0-2.4z"/></svg>
        555 382 9061
      </li>
      <li>
        <svg viewBox="0 0 24 24" aria-hidden="true"><path d="M2 5h20v14H2zm2 2v.5l8 5 8-5V7zm0 2.8V17h16V9.8l-8 5z"/></svg>
        hello@rjkstudio.com
      </li>
    </ul>

    <address class="address">
      <span>1420 Birchwood Drive</span>
      <span>Fairbanks, Alaska 99701</span>
      <span>www.rjkstudio.com</span>
    </address>

    <div class="stripes"><i class="red"></i><i class="yellow"></i><i class="navy"></i></div>
  </section>

  <section class="card card--back" aria-label="Business card back">
    <div class="brand"><span class="brand__mark"></span>RJK Entertainment</div>
  </section>
</main>
</body>
</html>
```